Banksia Hill Medical

Stationary design including letterhead A4, appointment card and with compliments
Updates

Hi Designers, we have some orange boxes in and around our main cross, we would like to see if those boxes could be used s part of the stationary design. Perhaps bouncing along the bottom of the page. Cheers Fay

Target Market(s)

We are a general practice with a wide range of patients.

Industry/Entity Type

Medical

Font styles to use
Serif
Sans Serif

Colors
9ccb3b
f37022
a64599

Requirements
Must have
• Address and contact details
Logo.Address
Shop 4, 28 Banksia Hill, KELLSBY SA 5190
Phone 08 85469931
Fax 08 85469978
web site - www.banksiahillmedical.com.au
Nice to have
• We have small boxes in our logo we would like used as a design element of the stationary.
Should not have
• Hard to read, script.

```html
<!DOCTYPE html>
<html lang="en">
<head>
<meta charset="utf-8">
<title>Banksia Hill Medical – Stationery</title>
<link rel="stylesheet" href="https://fonts.googleapis.com/css2?family=Roboto+Condensed:wght@400;700&display=swap">
<style>
  :root {
    --green: #7ee600;
    --orange: #f37022;
    --purple: #6a0aa6;
    --ink: #1a1a1a;
    --edge: #9a9a9a;
    --footer-yellow: #f5e34a;
    --paper: #ffffff;
  }
  * { margin: 0; padding: 0; box-sizing: border-box; }
  html, body { width: 947px; height: 1200px; overflow: hidden; background: var(--paper); }
  body { position: relative; font-family: "Roboto Condensed", Arial, sans-serif; color: var(--ink); }

  .page-art { position: absolute; inset: 0; }

  .brand-name {
    position: absolute; left: 383px; top: 118px; width: 140px;
    text-align: center; color: var(--purple); font-weight: 700;
    font-size: 22px; line-height: 1.1; text-transform: uppercase;
  }
  .contact-left {
    position: absolute; right: 583px; top: 93px; text-align: right; font-style: normal;
    color: var(--orange); font-size: 17px; line-height: 19px;
  }
  .contact-right {
    position: absolute; left: 564px; top: 96px; font-style: normal;
    color: var(--orange); font-size: 17px; line-height: 20px;
  }

  .card { position: absolute; background: var(--paper); border: 1px solid #bdbdbd; overflow: hidden; }
  .card::before, .card::after { content: ""; position: absolute; left: 0; right: 0; background: var(--purple); }
  .card::before { top: 0; height: 13px; }
  .card::after { bottom: 0; height: 17px; }

  .appointment-card { left: 244px; top: 395px; width: 343px; height: 221px; }
  .appointment-card .card-brand {
    position: absolute; left: 18px; top: 34px; width: 80px;
    color: var(--purple); font-weight: 700; font-size: 10px; line-height: 1.1; text-transform: uppercase;
  }
  .appointment-card .reminder { position: absolute; left: 255px; top: 27px; font-size: 13px; line-height: 16px; }
  .field { position: absolute; font-size: 14px; display: flex; align-items: flex-end; }
  .field .rule { border-bottom: 1px solid var(--ink); margin-left: 6px; height: 1px; }
  .field-with { left: 25px; top: 105px; }
  .field-with .rule { width: 175px; }
  .field-date { left: 27px; top: 150px; }
  .field-date .rule { width: 91px; }
  .field-time { left: 188px; top: 150px; }
  .field-time .rule { width: 108px; }
  .card-footer {
    position: absolute; left: 3px; right: 3px; bottom: 2px; z-index: 1;
    font-size: 6.6px; line-height: 12px; color: var(--orange); white-space: nowrap;
  }
  .card-footer .addr { color: var(--footer-yellow); }

  .compliments-card { left: 248px; top: 653px; width: 340px; height: 220px; }
  .compliments-card .heading { position: absolute; left: 0; right: 0; top: 22px; text-align: center; font-size: 20px; }
  .compliments-card .write-line { position: absolute; left: 12px; width: 306px; border-top: 1.5px solid var(--ink); }
</style>
</head>
<body>
  <svg class="page-art" width="947" height="1200" viewBox="0 0 947 1200" aria-hidden="true">
    <line x1="36" y1="0" x2="36" y2="1200" stroke="var(--edge)" stroke-width="1"/>
    <line x1="881" y1="0" x2="881" y2="1200" stroke="var(--edge)" stroke-width="1"/>
    <rect x="36" y="0" width="845" height="87" fill="var(--green)"/>
    <circle cx="453" cy="107" r="83" fill="var(--paper)"/>
    <path d="M36,1113 C300,1100 760,1090 850,1010 C875,985 881,950 881,893 L881,1200 L36,1200 Z" fill="var(--green)"/>
  </svg>

  <header>
    <div class="brand-name">Banksia Hill Medical</div>
    <address class="contact-left">
      Ph 08 85469931<br>
      Fax 08 85469978<br>
      www.banksiahillmedical.com.au
    </address>
    <address class="contact-right">
      Shop 4, 28 Banksia Hill<br>
      KELLSBY SA 5190
    </address>
  </header>

  <section class="card appointment-card">
    <div class="card-brand">Banksia Hill Medical</div>
    <p class="reminder">Don't Forget<br>your next<br>APPOINTMENT!</p>
    <div class="field field-with">APPOINTMENT WITH<span class="rule"></span></div>
    <div class="field field-date">DATE<span class="rule"></span></div>
    <div class="field field-time">TIME<span class="rule"></span></div>
    <p class="card-footer"><span class="addr">Shop 4, 28 Banksia Hill KELLSBY SA 5190</span> Ph 08 85469931 Fax 08 85469978 www.banksiahillmedical.com.au</p>
  </section>

  <section class="card compliments-card">
    <p class="heading">Complimant for you........</p>
    <span class="write-line" style="top:73px"></span>
    <span class="write-line" style="top:111px"></span>
    <span class="write-line" style="top:149px"></span>
    <span class="write-line" style="top:187px"></span>
  </section>
</body>
</html>
```